Postcard Design

We are a commercial real estate office located in Mount Kisco. We are holding a rather large event on August 6th for our tenants and in each give a way bag we would like to put a post card. This post card will feature 4 of our buildings on it. We would also like it to say something along the lines of Looking for Office, Medical, Warehouse or Retail space or know someone who is?? Fill out this post card with either your information or the information of a referral & send it back to receive a $25 Gift Card to Velvet Lanes, NY. The point of the post card is to get all guests to refer a friend who is looking for a space. We do need space for an address but we also do need a space on the back that has room for them to fill out all necessary information such as - Name - Email- Referral Name- Phone Number -
Also on the card we would like it to say for all space availabilities visit www.harlowestates.example along with some of our contact information. The building information is as follows - the picture with the flowers is 48 Calloway Rd, N. White Plains, the building with the grass round about in front of it is 210 S Pemberton Rd. Mount Kisco, the picture that has the close up of the building that is more of a square building is 207/209 S Pemberton Rd, Mount Kisco and the building with the clouds that is set far back is 561 North Pemberton Rd, Mount Kisco

NOTE I need all four buildings on the post card. Not just 1. Please list the building addresses by each picture

The name of our company is Harlow Estates - our phone number is 914 555 0187 and the contact for all inquiries is Owen Castellane

Target Market(s)

Brokers and business owners

Industry/Entity Type

Real Estate

Colors
0455a3
85abd2
3276b5

Requirements
Must have
• We are a commercial real estate office so we would like this post card to be catchy.

```html
<!DOCTYPE html>
<html lang="en">
<head>
<meta charset="utf-8">
<title>Harlow Estates – Referral Postcard</title>
<link href="https://fonts.googleapis.com/css2?family=Roboto+Condensed:ital,wght@0,400;0,700;1,400&display=swap" rel="stylesheet">
<style>
  :root {
    --brand-blue: #0455a3;
    --mid-blue: #3276b5;
    --soft-blue: #85abd2;
    --white: #ffffff;
    --ink: #111111;
  }
  * { box-sizing: border-box; margin: 0; padding: 0; }
  html, body { width: 1200px; height: 930px; overflow: hidden; background: var(--white); }
  .postcard {
    position: relative;
    width: 1200px;
    height: 930px;
    overflow: hidden;
    font-family: "Roboto Condensed", Arial, sans-serif;
    background: var(--white);
  }
  .backdrop { position: absolute; inset: 0; }

  .building {
    position: absolute;
    background: var(--white);
    padding: 9px;
    box-shadow: 0 4px 12px rgba(0,0,0,.35);
  }
  .building-photo { position: relative; width: 100%; height: 100%; }
  .building-address {
    position: absolute;
    top: 12px;
    right: 16px;
    color: var(--white);
    font-style: italic;
    font-size: 18px;
    text-shadow: 0 1px 3px rgba(0,0,0,.6);
    white-space: nowrap;
  }
  .building--calloway { left: 24px; top: 48px; width: 572px; height: 300px; transform: rotate(-2deg); }
  .building--calloway .building-photo { background: linear-gradient(180deg, #4f8fd0 0%, #6d8d5a 40%, #3f8a2c 75%, #5aa83a 100%); }
  .building--pemberton-207 { left: 594px; top: 26px; width: 570px; height: 300px; transform: rotate(2deg); }
  .building--pemberton-207 .building-photo { background: linear-gradient(180deg, #3f86d8 0%, #d8d4cc 35%, #8a6a55 70%, #6e7a4e 100%); }
  .building--pemberton-561 { left: 332px; top: 300px; width: 440px; height: 300px; transform: rotate(-3deg); }
  .building--pemberton-561 .building-photo { background: linear-gradient(180deg, #3b7ad0 0%, #b8cde6 28%, #4f7a38 45%, #8a3f2a 62%, #5a5a5a 85%, #3f3f3f 100%); }
  .building--pemberton-210 { left: 612px; top: 344px; width: 552px; height: 290px; transform: rotate(2deg); }
  .building--pemberton-210 .building-photo { background: linear-gradient(180deg, #4aa0e8 0%, #9fcaf0 35%, #d9c6a0 55%, #7a8a70 75%, #4f8a3a 100%); }

  .gift-sticker {
    position: absolute;
    left: 40px;
    top: 320px;
    width: 300px;
    height: 290px;
    transform: rotate(-7deg);
  }
  .gift-sticker svg { position: absolute; inset: 0; }
  .gift-amount {
    position: absolute;
    left: 0; right: 0;
    top: 70px;
    text-align: center;
    color: var(--white);
    font-weight: 700;
    font-size: 150px;
    line-height: 1;
    letter-spacing: -3px;
    text-shadow: 0 3px 6px rgba(0,0,0,.35);
  }

  .brand-block {
    position: absolute;
    left: 30px;
    top: 683px;
    width: 132px;
    height: 217px;
    display: flex;
    align-items: center;
    justify-content: center;
    text-align: center;
    background: var(--ink);
  }
  .brand-name {
    color: var(--white);
    font-size: 24px;
    font-weight: 400;
    letter-spacing: 2px;
    line-height: 1.2;
    text-transform: uppercase;
  }

  .headline {
    position: absolute;
    left: 213px;
    top: 680px;
    width: 970px;
    color: var(--brand-blue);
    font-weight: 700;
    font-size: 48px;
    line-height: 60px;
    text-transform: uppercase;
    word-spacing: 4px;
    white-space: nowrap;
  }
  .offer-text {
    position: absolute;
    left: 215px;
    top: 808px;
    width: 560px;
    color: var(--soft-blue);
    font-size: 25px;
    line-height: 31px;
    white-space: nowrap;
  }
  .contact-divider {
    position: absolute;
    left: 795px;
    top: 812px;
    width: 2px;
    height: 88px;
    background: var(--soft-blue);
  }
  .contact {
    position: absolute;
    left: 818px;
    top: 804px;
    color: var(--soft-blue);
    font-weight: 700;
    text-transform: uppercase;
    white-space: nowrap;
  }
  .contact-phone { font-size: 62px; line-height: 58px; }
  .contact-name { font-size: 43px; line-height: 46px; }
</style>
</head>
<body>
<main class="postcard">
  <svg class="backdrop" width="1200" height="930" viewBox="0 0 1200 930" aria-hidden="true">
    <rect width="1200" height="930" fill="var(--white)"/>
    <path d="M0 0 H1200 V640 C900 655 600 640 330 560 C200 520 90 470 0 440 Z" fill="var(--brand-blue)"/>
    <path d="M0 440 C90 470 200 520 330 560 C600 640 900 655 1200 640 V665 C900 675 580 665 330 600 C200 565 90 520 0 495 Z" fill="var(--soft-blue)"/>
  </svg>

  <figure class="building building--calloway">
    <div class="building-photo" role="img" aria-label="Photo of a round office building with flowering shrubs and lawn">
      <span class="building-address">48 Calloway Rd, N. White Plains</span>
    </div>
  </figure>
  <figure class="building building--pemberton-207">
    <div class="building-photo" role="img" aria-label="Close-up photo of a square three-storey office building with a tree">
      <span class="building-address">207/209 S Pemberton Rd, Mount Kisco</span>
    </div>
  </figure>
  <figure class="building building--pemberton-210">
    <div class="building-photo" role="img" aria-label="Photo of a low office building behind a grass roundabout">
      <span class="building-address">210 S Pemberton Rd. Mount Kisco</span>
    </div>
  </figure>
  <figure class="building building--pemberton-561">
    <div class="building-photo" role="img" aria-label="Photo of a brick warehouse building set back behind a parking lot under clouds">
      <span class="building-address">561 North Pemberton Rd, Mount Kisco</span>
    </div>
  </figure>

  <div class="gift-sticker">
    <svg width="300" height="290" viewBox="0 0 300 290" aria-hidden="true">
      <defs>
        <linearGradient id="stickerFill" x1="0" y1="0" x2="1" y2="1">
          <stop offset="0" stop-color="#2b5fb8"/>
          <stop offset="1" stop-color="#0a2f7a"/>
        </linearGradient>
      </defs>
      <path d="M70 8 H262 Q292 8 292 38 V252 Q292 282 262 282 H38 Q8 282 8 252 V70 Z" fill="var(--white)" stroke="#cfd8e6" stroke-width="2"/>
      <path d="M76 22 H256 Q278 22 278 44 V246 Q278 268 256 268 H44 Q22 268 22 246 V76 Z" fill="url(#stickerFill)"/>
      <path d="M8 70 L70 8 C60 40 50 60 8 70 Z" fill="#e8edf4" stroke="#b9c6d8" stroke-width="1.5"/>
    </svg>
    <div class="gift-amount">$25</div>
  </div>

  <div class="brand-block">
    <span class="brand-name">Harlow<br>Estates</span>
  </div>

  <h1 class="headline">Looking for office, medical, warehouse<br>or retail space or know someone who is?</h1>

  <p class="offer-text">Fill out this post card with your information and the<br>information of a referral, send it back to receive a<br>$25 Gift Card to Velvet Lanes, NY</p>

  <div class="contact-divider"></div>
  <div class="contact">
    <div class="contact-phone">914 555 0187</div>
    <div class="contact-name">Owen Castellane</div>
  </div>
</main>
</body>
</html>
```